stationary for home builder
Birchwood Custom Homes, Inc.
Project: stationary for home builder
stationary for home builder - Real Estate
Creative Brief
Professional
Dale Morrow
President
4200 Tern Avenue, suite 310 Harbor Point, CA 94107
bchdalemorrow@mailvista.test

```html
<!DOCTYPE html>
<html lang="en">
<head>
<meta charset="utf-8">
<title>Birchwood Custom Homes, Inc. — Business Card</title>
<link href="https://fonts.googleapis.com/css2?family=Cinzel:wght@400&family=Lato:wght@400&display=swap" rel="stylesheet">
<style>
  :root {
    --bg: #8a8b8d;
    --red: #c8161d;
    --red-dark: #9e0f14;
    --red-light: #e0262c;
    --grey: #a7a9ac;
    --grey-dark: #6d6e71;
    --ink: #4a4a4a;
    --white: #ffffff;
  }
  * { margin: 0; padding: 0; box-sizing: border-box; }
  html, body { width: 1200px; height: 908px; overflow: hidden; }
  body { background: var(--bg); position: relative; font-family: "Lato", sans-serif; }

  .card {
    position: absolute;
    left: 250px;
    width: 700px;
    height: 400px;
    border-radius: 22px;
    overflow: hidden;
  }
  .card--front {
    top: 40px;
    background: linear-gradient(135deg, var(--red-light) 0%, var(--red) 45%, var(--red-dark) 100%);
  }
  .card--back { top: 468px; background: var(--white); }

  .company-name {
    position: absolute;
    display: flex;
    align-items: center;
    font-family: "Lato", sans-serif;
    font-weight: 400;
    line-height: 1;
    white-space: nowrap;
  }
  .company-name .mark { display: block; flex: none; }

  .front-name {
    right: 60px;
    top: 180px;
    font-size: 34px;
    gap: 14px;
    color: var(--white);
  }
  .front-name .mark { width: 22px; height: 22px; background: var(--white); }

  .back-name {
    left: 42px;
    top: 300px;
    font-size: 26px;
    gap: 10px;
    color: var(--red);
  }
  .back-name .mark { width: 18px; height: 18px; background: var(--red); }

  .swoosh { position: absolute; inset: 0; width: 700px; height: 400px; }

  .contact {
    position: absolute;
    left: 260px;
    top: 70px;
    color: var(--ink);
  }
  .contact .person {
    font-family: "Cinzel", serif;
    font-size: 26px;
    color: var(--red);
    letter-spacing: 1px;
    border-bottom: 1px solid #c9c9c9;
    padding-bottom: 2px;
  }
  .contact .title {
    font-family: "Cinzel", serif;
    font-size: 12px;
    letter-spacing: 2px;
    color: var(--grey-dark);
    margin-top: 4px;
  }
  .contact .address { font-size: 13px; line-height: 17px; margin-top: 12px; }
  .contact ul { list-style: none; margin-top: 8px; }
  .contact li { display: flex; align-items: center; gap: 7px; font-size: 13px; line-height: 20px; }
  .contact li svg { width: 13px; height: 13px; flex: none; }
</style>
</head>
<body>

<section class="card card--front" aria-label="Card front">
  <div class="company-name front-name">
    <span class="mark" aria-hidden="true"></span>
    <span>Birchwood Custom Homes, Inc.</span>
  </div>
</section>

<section class="card card--back" aria-label="Card back">
  <svg class="swoosh" viewBox="0 0 700 400" aria-hidden="true">
    <path d="M622,0 C585,225 505,360 320,400 L390,400 C530,362 600,235 642,0 Z" fill="var(--grey)"/>
    <path d="M655,0 C615,230 545,360 410,400 L700,400 L700,0 Z" fill="var(--red)"/>
  </svg>

  <div class="contact">
    <div class="person">DALE MORROW</div>
    <div class="title">PRESIDENT</div>
    <div class="address">
      4200 Tern Avenue, suite 310<br>
      Harbor Point, CA 94107
    </div>
    <ul>
      <li>
        <svg viewBox="0 0 14 14"><circle cx="7" cy="7" r="7" fill="var(--red)"/><path d="M4.5 3.5 L6 3.5 L6.6 5.4 L5.7 6.1 C6.1 7 7 7.9 7.9 8.3 L8.6 7.4 L10.5 8 L10.5 9.5 C7 9.8 4.2 7 4.5 3.5 Z" fill="var(--white)"/></svg>
        555 310 2218
      </li>
      <li>
        <svg viewBox="0 0 14 14"><circle cx="7" cy="7" r="7" fill="var(--red)"/><path d="M4.5 3.5 L6 3.5 L6.6 5.4 L5.7 6.1 C6.1 7 7 7.9 7.9 8.3 L8.6 7.4 L10.5 8 L10.5 9.5 C7 9.8 4.2 7 4.5 3.5 Z" fill="var(--white)"/></svg>
        555 310 6642
      </li>
      <li>
        <svg viewBox="0 0 14 14"><circle cx="7" cy="7" r="7" fill="var(--red)"/><rect x="3.5" y="4.5" width="7" height="5" fill="var(--white)"/><path d="M3.5 4.5 L7 7.3 L10.5 4.5" fill="none" stroke="var(--red)" stroke-width="0.8"/></svg>
        bchdalemorrow@mailvista.test
      </li>
    </ul>
  </div>

  <div class="company-name back-name">
    <span class="mark" aria-hidden="true"></span>
    <span>Birchwood Custom Homes, Inc.</span>
  </div>
</section>

</body>
</html>
```